Business Card/ Email Signature Design Project

I am an Interior Designer. I need a business card that looks sophisticated stylish but simple in design. My work covers space design/ interior architecture/ furniture design/ product development & styling.

I have a very specific brief and know mostly what I want. I'm hoping to work with someone who can translate my ideas.

My branding should have a strong focus on my name, the majority of my work is referral based.
I'm keen to keep a monochromatic colour scheme: dark charcoal/ black/ white/ embossing/ silver. I'm not suggesting we use all that I've listed, they are possible ideas at this stage. I will need to be mindful of printing costs an also how I make the design work across, cards, letter heads, email logo and web design.

Theory behind images sent below;
1-Rug Image_(minus boarder) I was thinking this image could be used on the back of the card with my contact details over. I like that the lines are almost hand drawn and start to look free form. It's a subtle contrast to a more formal front of the card with my name.
2_Owen Ratley_I really like the orientation, the proportion of font on the card, the colour and the font. I like the lower case for my name and the upper case for 'Interior Design'. Not sure if it should be 'Interior Designer or Interior Design' at this stage, was leaning towards 'Interior Design'. Was thinking the 'i' and 'd' in my surname could be the colour eg 'silver'?? We can decide on this once we see it.

Look forward to hearing from you.
Cheers,
Noreen Bastoli

Industry/Entity Type

Printing

Logo Text

Noreen Bastoli Interior Design

```html
<!DOCTYPE html>
<html lang="en">
<head>
<meta charset="utf-8">
<title>Noreen Bastoli – Interior Designer Business Card</title>
<link rel="stylesheet" href="https://fonts.googleapis.com/css2?family=Arimo:wght@400&family=Questrial&display=swap">
<style>
  :root {
    --page: #ffffff;
    --charcoal-edge: #48484b;
    --charcoal-mid: #7d7d82;
    --name-ink: #111111;
    --silver-light: #e2e3e6;
    --linen: #e7e5e0;
    --linen-light: #f1efeb;
    --contact-ink: #0d0d0d;
  }
  html, body {
    margin: 0;
    padding: 0;
    width: 982px;
    height: 1200px;
    overflow: hidden;
    background: var(--page);
  }
  .canvas {
    position: relative;
    width: 982px;
    height: 1200px;
  }
  .card {
    position: absolute;
    left: 93px;
    width: 810px;
    height: 461px;
    overflow: hidden;
  }
  .card--front {
    top: 92px;
    background: linear-gradient(90deg,
      var(--charcoal-edge) 0%,
      var(--charcoal-mid) 34%,
      #6c6c70 62%,
      var(--charcoal-edge) 100%);
  }
  .brand {
    position: absolute;
    left: 0;
    right: 0;
    top: 150px;
    text-align: center;
    font-family: "Arimo", Arial, sans-serif;
  }
  .brand__name {
    margin: 0;
    font-size: 60px;
    font-weight: 400;
    line-height: 1;
    letter-spacing: 0.5px;
    color: var(--name-ink);
  }
  .brand__title {
    margin: 10px 0 0;
    font-size: 34px;
    font-weight: 400;
    line-height: 1;
    letter-spacing: 2px;
    color: var(--silver-light);
    opacity: 0.85;
  }
  .card--back {
    top: 592px;
    background: var(--linen);
  }
  .rug-texture {
    position: absolute;
    inset: 0;
    background: radial-gradient(ellipse at 50% 45%, var(--linen-light) 0%, var(--linen) 60%, #dcdad5 100%);
  }
  .contact {
    position: absolute;
    left: 0;
    right: 0;
    top: 104px;
    margin: 0;
    padding: 0;
    list-style: none;
    text-align: center;
    font-family: "Questrial", "Century Gothic", sans-serif;
    font-size: 42px;
    line-height: 60px;
    letter-spacing: 0.5px;
    color: var(--contact-ink);
  }
</style>
</head>
<body>
<main class="canvas">
  <section class="card card--front">
    <div class="brand">
      <h1 class="brand__name">Noreen Bastoli</h1>
      <p class="brand__title">INTERIOR DESIGNER</p>
    </div>
  </section>

  <section class="card card--back">
    <div class="rug-texture" role="img" aria-label="Woven linen rug texture with free-form hand-drawn grey line pattern"></div>
    <ul class="contact">
      <li>P.O Box 214 Kelmscott VIC. 3118</li>
      <li>Email: interiors@noreenbastoli.com</li>
      <li>Web: www.noreenbastoli.com</li>
      <li>Mobile: 0491 570 156</li>
    </ul>
  </section>
</main>
</body>
</html>
```